50's-style gig poster for a birthday bash

My wife was born in 1957 and is turning 57 next month. I'm throwing a surprise party for her, and thought it would be fun to have a 18x24 poster printed and framed for the event. Attached is a poster from a Rolf Tesker gig in 1957. I'd like something like this, with a tinted B&W head shot of my wife, with similar fonts and background color schemes. The copy will be GRETA at the top (where the name ROLF appears), with 57X57 under it, and the word Celebration where the word Quartet currently appears. The rest of the copy will be provided to you. Thanks for your interest and I look forward to working with you.

```html
<!DOCTYPE html>
<html lang="en">
<head>
<meta charset="utf-8">
<title>The Greta Celebration</title>
<link href="https://fonts.googleapis.com/css2?family=Abril+Fatface&family=Jost:wght@500;600&family=Libre+Bodoni:wght@700&family=Playfair+Display:ital,wght@1,900&family=PT+Sans&family=Josefin+Sans:wght@600&display=swap" rel="stylesheet">
<style>
  :root {
    --cream: #fdf8d8;
    --navy: #37407c;
    --brick: #d8452a;
    --ink: #000;
    --paper: #fff;
    --photo-light: #b9d3f0;
    --photo-dark: #3c6eb4;
  }
  html, body { margin: 0; padding: 0; overflow: hidden; }
  .poster {
    position: relative;
    width: 913px; height: 1200px;
    background: var(--cream);
    overflow: hidden;
  }
  .stripe { position: absolute; top: 25px; height: 1152px; }
  .stripe--navy { background: var(--navy); }
  .stripe--brick { background: var(--brick); }

  .title-the {
    position: absolute; left: 62px; top: 46px;
    font: italic 500 40px/1 "Jost", sans-serif;
    color: var(--paper); letter-spacing: -2px;
    transform: scaleX(0.85) skewX(-8deg); transform-origin: left top;
  }
  .title-letter {
    position: absolute; top: 82px; width: 151px;
    text-align: center;
    font: 600 182px/1 "Jost", sans-serif;
    color: var(--paper);
    text-shadow: 4px 4px 0 var(--ink);
    transform: scaleX(0.74);
  }
  .celebration {
    position: absolute; left: 462px; top: 264px;
    font: 70px/1 "Abril Fatface", serif;
    color: var(--paper);
    text-shadow: 4px 4px 0 var(--ink);
    transform: rotate(-6deg); transform-origin: left center;
    letter-spacing: -1px;
    white-space: nowrap;
  }
  .lineup {
    position: absolute; left: 472px; width: 400px; top: 346px;
    margin: 0; padding: 0; list-style: none; text-align: center;
    font: 700 34px/46.5px "Libre Bodoni", serif;
    color: var(--paper);
    text-shadow: 3px 3px 0 var(--ink);
  }
  .portrait {
    position: absolute; left: 70px; top: 345px;
    width: 363px; height: 455px;
    transform: rotate(-5deg);
  }
  .portrait__shadow {
    position: absolute; left: -11px; top: 11px; width: 100%; height: 100%;
    background: var(--ink);
  }
  .portrait__photo {
    position: absolute; inset: 0;
    background: linear-gradient(160deg, var(--photo-light), var(--photo-dark));
  }
  .date-badge {
    position: absolute; left: 516px; top: 696px;
    width: 272px; height: 198px;
    border: 3px solid var(--ink); border-radius: 50%;
    background: var(--paper);
    display: flex; flex-direction: column; align-items: center; justify-content: center;
    font: 32px/1.38 "PT Sans", sans-serif;
    color: var(--navy);
  }
  .date-badge__time { color: var(--ink); }
  .also {
    position: absolute; left: 140px; top: 856px;
    font: italic 900 44px/1 "Playfair Display", serif;
    color: var(--paper);
    text-shadow: 3px 3px 0 var(--ink);
    white-space: nowrap;
  }
  .support {
    position: absolute; left: 40px; top: 925px; width: 833px;
    text-align: center; white-space: nowrap;
    font: italic 900 61px/1 "Playfair Display", serif;
    color: var(--paper);
    text-shadow: 4px 4px 0 var(--ink);
  }
  .venue {
    position: absolute; left: 69px; top: 1019px;
    width: 776px; height: 104px;
    background: var(--paper);
    box-shadow: 5px 5px 0 var(--ink);
    text-align: center;
  }
  .venue__name {
    margin: 10px 0 0;
    font: 54px/1 "Abril Fatface", serif;
    color: var(--ink); letter-spacing: 3px;
  }
  .venue__address {
    margin: 6px 0 0;
    font: 600 31px/1 "Josefin Sans", sans-serif;
    color: var(--navy); letter-spacing: 1px;
  }
</style>
</head>
<body>
<div class="poster">
  <div class="stripe stripe--navy" style="left:26px;width:150px"></div>
  <div class="stripe stripe--brick" style="left:203px;width:152px"></div>
  <div class="stripe stripe--navy" style="left:381px;width:152px"></div>
  <div class="stripe stripe--brick" style="left:558px;width:152px"></div>
  <div class="stripe stripe--navy" style="left:736px;width:151px"></div>

  <div class="title-the">THE</div>
  <div class="title-letter" style="left:26px">G</div>
  <div class="title-letter" style="left:203px">R</div>
  <div class="title-letter" style="left:381px">E</div>
  <div class="title-letter" style="left:558px">T</div>
  <div class="title-letter" style="left:736px">A</div>

  <div class="celebration">Celebration</div>

  <ul class="lineup">
    <li>Featuring:</li>
    <li>The Ashcrofts</li>
    <li>The Pembertons</li>
    <li>The Dellacortes</li>
    <li>The Whitfield-Ames</li>
    <li>The Brannigans</li>
    <li>The Kettleworths</li>
  </ul>

  <div class="portrait">
    <div class="portrait__shadow"></div>
    <div class="portrait__photo" role="img" aria-label="Blue-tinted portrait photo of Greta, smiling and looking upward"></div>
  </div>

  <div class="date-badge">
    <span>One Night Only</span>
    <span>April 4, 2014</span>
    <span class="date-badge__time">6 PM</span>
  </div>

  <div class="also">Also Appearing</div>
  <div class="support">The Fizzlers &amp; Dot Vance</div>

  <div class="venue">
    <p class="venue__name">CAFÉ MARCELINE</p>
    <p class="venue__address">1418 Cedar Lane, Harlow Springs, California</p>
  </div>
</div>
</body>
</html>
```